Elegant and modern Wedding Photography brochure

My existing brochure (attached) needs a major facelift. This is one of the main selling tools - it gets emailed to my clients when they make an equiry on what packages i offer and it is printed out and walked through at our first meeting. This brochure is as critical as my website - it needs to sing!

I'm looking for an eye-catching design that says:
Elegant
Modern
Clean
Crisp
Not cutesy or lovey-dovey thanks - we are more sophisticated and professional than that.

Update images to some of the latest weddings I've shot also. Let me know files and resolution you need. I've enabled right-click to download images on my site for a limited time. Please note that I retain copyright and will pursue any breeches.

Http://www.carlathornbey.com/Melbourne-wedding-photography
Updates

Thanks for all of your designs! Will take a few days to decide.

Target Market(s)

Australian Women aged 24-44

Industry/Entity Type

Wedding

Font styles to use
Other font styles liked:
• Century Gothic

Requirements
Must have
• Easy to print - does not have to be 6 A4 pages like the existing brochure
Nice to have
• Some full page images - The photos are supposed to be the hero here :-)
Should not have
• Not cutesy or lovey-dovey thanks - we are more sophisticated and professional than that.

No black backgrounds, I prefer a white thanks

No images in organic shaped boxes (like the rectangles in the logo - no thanks).
Keep the lines straight and sharp

```html
<!DOCTYPE html>
<html lang="en">
<head>
<meta charset="utf-8">
<title>Carla Thornbey – Wedding Brochure</title>
<link href="https://fonts.googleapis.com/css2?family=Didact+Gothic&display=swap" rel="stylesheet">
<style>
:root{
  --bg:#e9e7e4;
  --paper:#ffffff;
  --plum:#9c3f8f;
  --magenta:#a3247f;
  --ink:#4a4a4a;
  --ink-soft:#777;
  --mint:#8fd3b8;
  --gold:#cfc63c;
  --orchid:#c07ab6;
  --photo-warm:linear-gradient(160deg,#c9b9a6,#8a7a66);
  --photo-grey:linear-gradient(160deg,#d8d8d8,#7e7e7e);
  --photo-green:linear-gradient(160deg,#a79a5c,#5e5a32 55%,#d6d2c8);
}
*{box-sizing:border-box;margin:0;padding:0}
html,body{width:1200px;height:760px;overflow:hidden;background:var(--bg)}
body{font-family:"Didact Gothic",sans-serif;color:var(--ink);position:relative}
.page{position:absolute;background:var(--paper);overflow:hidden;box-shadow:0 2px 6px rgba(0,0,0,.18)}
.photo{position:absolute}
.photo--warm{background:var(--photo-warm)}
.photo--grey{background:var(--photo-grey)}
.photo--green{background:var(--photo-green)}
.spine{position:absolute;background:var(--plum)}
.heading{position:absolute;color:var(--magenta);font-weight:400;line-height:1}
.label{color:var(--magenta);font-size:5.6px;letter-spacing:.2px;text-transform:uppercase;margin-top:5px}
.body{font-size:5.4px;line-height:1.55;color:var(--ink)}
.col{position:absolute}
.folio{position:absolute;bottom:8px;left:0;right:0;text-align:center;font-size:4px;color:var(--ink-soft)}
.brand{position:absolute;display:flex;align-items:center;gap:3px;font-size:7px;color:var(--magenta)}
.brand-mark{width:7px;height:7px;background:var(--magenta)}
.brand--light{color:#fff}
.brand--light .brand-mark{background:#fff}
.overlay-text{position:absolute;color:#fff;line-height:1}

/* packages */
.package{position:absolute;left:20px;width:182px;color:#fff;padding:5px 7px}
.package--signature{top:54px;height:83px;background:var(--orchid)}
.package--platinum{top:139px;height:65px;background:var(--mint)}
.package--gold{top:206px;height:57px;background:var(--gold)}
.package h3{font-weight:400;font-size:10px}
.package .price{font-size:4.5px;opacity:.9;margin-bottom:4px}
.package ul{list-style:none;font-size:3.6px;line-height:1.5;columns:2;column-gap:8px}
.package li::before{content:"• "}

.fees li{list-style:none;font-size:4.2px;line-height:1.55;color:var(--ink)}
.fees .fee{color:var(--magenta);text-transform:uppercase}
</style>
</head>
<body>

<!-- Cover -->
<section class="page" style="left:32px;top:62px;width:220px;height:311px">
  <div class="photo photo--grey" style="left:0;top:0;width:116px;height:115px" role="img" aria-label="Black and white portrait of the bride and groom"></div>
  <div class="photo photo--warm" style="left:120px;top:0;width:100px;height:115px" role="img" aria-label="Bridal bouquet resting on a chair"></div>
  <div class="spine" style="left:0;top:115px;width:220px;height:5px"></div>
  <div class="photo photo--warm" style="left:0;top:120px;width:220px;height:191px" role="img" aria-label="Smiling bride in her veil"></div>
  <p class="overlay-text" style="left:126px;top:226px;font-size:15px;line-height:.95">Love is all<br>you need</p>
  <div class="brand brand--light" style="left:20px;top:290px"><span class="brand-mark"></span>Carla Thornbey</div>
</section>

<!-- Page 2 -->
<section class="page" style="left:266px;top:62px;width:220px;height:311px">
  <h2 class="heading" style="left:19px;top:35px;font-size:12.5px;line-height:.95">Carla's<br>approach…</h2>
  <p class="heading" style="left:19px;top:63px;font-size:7px;font-style:italic;color:var(--magenta)">Enjoy your special day!</p>
  <div class="col body" style="left:19px;top:80px;width:88px">
    <p class="label">Style &amp; Approach</p>
    <p>Carla can observe and capture your wedding day in the background, quickly and quietly taking photojournalistic pictures rather than directing it if you prefer. Or she can confidently play the role of Art Director and instruct beautiful poses. Either way, what is most important is that her clients are relaxed and having a really great time on their wedding day!</p>
    <p class="label">Formal Photography</p>
    <p>Many of Carla's clients book her because of the easy-going approach she has. They can get on with having a great time on their day without worrying about formal photography. However, there are occasions when clients do want formal family pictures, and</p>
  </div>
  <div class="photo photo--grey" style="left:112px;top:18px;width:88px;height:146px" role="img" aria-label="Bride in veil holding a bouquet"></div>
  <div class="col body" style="left:112px;top:168px;width:90px">
    <p>Carla is more than happy to accommodate their requests. In order to keep the disruption on the day to a minimum, we recommend that Carla photographs no more than 6 groups, and a select number of the special couple.</p>
    <p class="label">Image Presentation</p>
    <p>The most professional way of presenting clients with their photographs is in an elegantly designed photo book.</p>
  </div>
  <p class="folio">2</p>
</section>
<div class="spine" style="left:486px;top:62px;width:4px;height:311px"></div>

<!-- Page 3 -->
<section class="page" style="left:490px;top:62px;width:214px;height:311px">
  <div class="col body" style="left:14px;top:18px;width:96px">
    <p>Carla's clients only pay one fixed price for the photography, regardless of how many images taken. There are no hard sell procedures to go through, and the completed book is prepared within 2-6 weeks after the wedding day.</p>
  </div>
  <div class="col body" style="left:108px;top:18px;width:96px">
    <p class="label" style="margin-top:0">Time of Year</p>
    <p>Signature pictures can be taken on overcast days or winter months. Don't worry if the sky is not perfectly blue. In the end, regardless of the weather – it's the timeless mood of the day that Carla strives to capture.</p>
  </div>
  <div class="photo photo--green" style="left:0;top:108px;width:214px;height:203px" role="img" aria-label="Bride and groom under a willow tree by a fallen log"></div>
</section>

<!-- Page 4 -->
<section class="page" style="left:718px;top:62px;width:217px;height:311px">
  <div class="photo photo--green" style="left:0;top:0;width:217px;height:190px" role="img" aria-label="Laughing bride with her bridesmaids"></div>
  <p class="overlay-text" style="left:19px;top:38px;font-size:11px;line-height:.95">What client's<br>are saying..</p>
  <div class="col body" style="left:19px;top:210px;width:86px">
    <p>"Words can't express my thanks Carla, I am absolutely in awe of my photos! You've captured my wedding day perfectly; couldn't ask for anything more."</p>
    <p style="color:var(--magenta)">-MEG, SEDDON</p>
  </div>
  <div class="col body" style="left:114px;top:210px;width:88px">
    <p>"Thanks so much for photographing our special day, you did an amazing job and made everyone feel so comfortable. The amount of comments we have had on the photos so far has been wonderful and we couldn't be happier!"</p>
    <p style="color:var(--magenta)">-JOANNE, KINGSVILLE</p>
  </div>
  <p class="folio">4</p>
</section>
<div class="spine" style="left:935px;top:62px;width:4px;height:311px"></div>

<!-- Page 5 -->
<section class="page" style="left:939px;top:62px;width:221px;height:311px;background:linear-gradient(135deg,#fbf4f4,#efdede 55%,#b8a8a4)" role="img" aria-label="Soft background of pale roses in a glass jar">
  <h2 class="heading" style="left:20px;top:16px;font-size:12.5px">Wedding Packages</h2>
  <p class="heading" style="left:20px;top:33px;font-size:6.5px;font-style:italic;color:var(--ink-soft)">Pricelist 2013</p>
  <div class="package package--signature">
    <h3>Signature</h3>
    <p class="price">Price: $3650 ($5540 value)</p>
    <ul>
      <li>Up to 8 hrs of coverage</li>
      <li>Signature Grand album with lay flat pages, choice of linen or leather cover, presentation box and embossing up to 52 pages</li>
      <li>Custom thank you cards with envelopes</li>
      <li>Client for life sitting fees</li>
      <li>Second photographer</li>
      <li>Pre-wedding shoot</li>
      <li>Web gallery online for 6 weeks</li>
      <li>High resolution digital negatives</li>
    </ul>
  </div>
  <div class="package package--platinum">
    <h3>Platinum</h3>
    <p class="price">Price: $2550 ($3440 value)</p>
    <ul>
      <li>Up to 6 hrs of coverage</li>
      <li>Regular album with lay flat pages, printed cover, presentation box, up to 40 pages</li>
      <li>Slideshow</li>
      <li>Pre-wedding shoot</li>
      <li>Web gallery online for 6 weeks</li>
      <li>High resolution digital negatives</li>
    </ul>
  </div>
  <div class="package package--gold">
    <h3>Gold</h3>
    <p class="price">Price: $1650 ($2080 value)</p>
    <ul>
      <li>Up to 4 hrs of coverage</li>
      <li>Regular album with lay flat pages, printed cover, presentation box, up to 30 pages</li>
      <li>Web gallery online for 6 weeks</li>
      <li>High resolution digital negatives</li>
    </ul>
  </div>
  <p class="body" style="position:absolute;left:20px;top:281px;font-size:3.4px;color:#fff">* Approx. 1200x1800 jpeg at 240 pixels per inch, suitable for printing. No watermarks.</p>
  <p class="folio" style="color:#fff">5</p>
</section>

<!-- Page 6 -->
<section class="page" style="left:266px;top:399px;width:220px;height:311px">
  <div class="photo photo--green" style="left:0;top:0;width:130px;height:75px" role="img" aria-label="Couple standing beneath willow branches"></div>
  <div class="photo photo--warm" style="left:132px;top:0;width:88px;height:75px" role="img" aria-label="Close portrait of the bride"></div>
  <h2 class="heading" style="left:19px;top:96px;font-size:12px;line-height:.95">À la carte<br>Fees to consider</h2>
  <ul class="fees col" style="left:21px;top:132px;width:190px">
    <li class="fee">Engagement session/pre-wedding shoot</li>
    <li>$290 for up to 2 hours of photography on location</li>
    <li class="fee">Digital negatives $490</li>
    <li class="fee">Extended coverage $160 per hour</li>
    <li class="fee">Web gallery &amp; social posting $160</li>
    <li class="fee">Slideshow $250</li>
    <li class="fee">Second photographer $590</li>
    <li class="fee">Client for life</li>
    <li>No sitting fees for portrait sessions – Anniversaries, family portraits, etc: $390</li>
    <li class="fee">Photo enlargements</li>
    <li>- Quality custom archival prints in a variety of sizes 5x7 up to 8x10 $25, 12.5x18.5 $50</li>
    <li>- Stretched canvas prints for your wall. Various sizes available from 16"x20" starting at $395 through to 60"x96" $1500</li>
    <li>Plus many other options!</li>
    <li class="fee">Professionally edited album (regular) $790</li>
    <li class="fee">Album upgrade from regular to signature grand</li>
    <li>- From Gold Package to Signature Grand: $1150</li>
    <li>- From Platinum Package to Signature Grand: $650</li>
    <li class="fee">Custom thank-you cards</li>
    <li>$150 for 50 cards (174mm x 123mm) including envelopes</li>
  </ul>
  <p class="folio">6</p>
</section>
<div class="spine" style="left:486px;top:399px;width:4px;height:311px"></div>

<!-- Page 7 -->
<section class="page" style="left:490px;top:399px;width:213px;height:311px">
  <div class="brand" style="left:75px;top:17px"><span class="brand-mark"></span>Carla Thornbey</div>
  <h2 class="heading" style="left:14px;top:50px;font-size:11px;line-height:.95">HOW DO YOU WANT<br>TO REMEMBER…</h2>
  <div class="photo photo--grey" style="left:0;top:75px;width:213px;height:142px" role="img" aria-label="Black and white portrait of the smiling couple"></div>
  <p class="overlay-text" style="left:62px;top:196px;font-size:11px;color:var(--magenta)">YOUR SPECIAL DAY?</p>
  <div class="col body" style="left:14px;top:232px;width:188px;font-size:4.6px">
    <p>Elegant, stunning, fuss-free photography that doesn't cost the earth will capture those memories for a lifetime!</p>
    <p>Wedding photography packages start from $1650 and are fully inclusive of fun filled creative &amp; journalistic coverage, digital negatives and professionally edited album.</p>
    <p style="margin-top:5px">Contact Carla today to arrange an informal catch-up, discuss your requirements and find out more about the <span style="color:var(--magenta)">early booking bonus!</span></p>
  </div>
  <p class="folio">7</p>
</section>

<!-- Back cover -->
<section class="page" style="left:718px;top:399px;width:220px;height:311px">
  <div class="photo photo--grey" style="left:0;top:0;width:220px;height:235px" role="img" aria-label="Black and white bride looking down at her bouquet"></div>
  <div class="spine" style="left:0;top:235px;width:220px;height:5px"></div>
  <div class="brand" style="left:88px;top:250px;font-size:6px"><span class="brand-mark" style="width:6px;height:6px"></span>Carla Thornbey</div>
  <div class="col" style="left:0;top:269px;width:220px;text-align:center;font-size:4.4px;line-height:1.7">
    <p style="margin-bottom:4px">Albert Lane, Seddon, VIC, 3011</p>
    <p style="color:var(--magenta)">www.carlathornbey.com</p>
    <p style="color:var(--magenta)">hello@carlathornbey.com</p>
    <p style="color:var(--magenta)">Mobile: 0400 582 107</p>
  </div>
</section>

</body>
</html>
```